Stonelynk Business Card Design

The Stonelynk Co is an aggregate (crushing) equipment dealer serving Western Canadian provinces. Stonelynk is a distributor of aggregate equipment for different manufacturers.

We are looking to change and update the existing business card which has been used since the existence of the company. A copy of existing card has been attached for reference. The Stonelynk Co logo we want to remain the same and we want the green color to remain the same.

We are wanting something new with a different look. A refreshing card to show a new modern and updated look. No longer wanting to have the manufacturers on the back of the card but something more like our logo on the back of the card with a statement like "Crushing Solutions"

ideas could be:
- card can be different colors on front and back
- front or reverse of the card could possibly be the green color with the logo in black

Target Market(s)

Owners of Aggregate/Crushing companies

Requirements
Must have
• - logo to remain same along with same font within logo
• - green color to remain same
Nice to have
• as noted above under project description
Should not have

```html
<!DOCTYPE html>
<html lang="en">
<head>
<meta charset="utf-8">
<title>The Stonelynk Co — Business Card</title>
<link rel="stylesheet" href="https://fonts.googleapis.com/css2?family=Open+Sans:wght@400;600;700&display=swap">
<style>
  :root {
    --bg-top: #eef1f6;
    --bg-bottom: #a9b0bd;
    --green: #7b8427;
    --green-light: #8c9630;
    --green-line: #9aa53d;
    --paper: #f4f4f2;
    --ink: #1e1e1e;
    --white: #ffffff;
    --back-text: #e6e8d6;
  }
  * { box-sizing: border-box; margin: 0; padding: 0; }
  html, body { width: 1200px; height: 1000px; overflow: hidden; }
  body {
    background: linear-gradient(160deg, var(--bg-top) 0%, var(--bg-bottom) 100%);
    font-family: "Open Sans", Arial, sans-serif;
    position: relative;
  }
  .card {
    position: absolute;
    width: 560px;
    height: 320px;
    overflow: hidden;
    box-shadow: 0 18px 30px rgba(40, 48, 60, 0.28);
  }

  /* Back of card */
  .card-back {
    left: 560px;
    top: 130px;
    background: var(--green);
    color: var(--back-text);
  }
  .card-back .brand {
    position: absolute;
    left: 150px;
    top: 92px;
    display: flex;
    align-items: center;
    gap: 14px;
  }
  .card-back .brand-dot {
    width: 34px; height: 34px;
    border-radius: 50%;
    background: var(--back-text);
  }
  .card-back .brand-name {
    font-weight: 700;
    font-size: 22px;
    letter-spacing: 0.5px;
    color: var(--back-text);
  }
  .card-back .website {
    position: absolute;
    left: 198px;
    top: 140px;
    font-size: 15px;
    letter-spacing: 0.6px;
  }
  .card-back .rule-top {
    position: absolute;
    left: 300px; top: 128px;
    width: 230px; height: 1px;
    background: var(--back-text);
    opacity: 0.8;
  }
  .card-back .rule-bottom {
    position: absolute;
    left: 30px; top: 250px;
    width: 260px; height: 1px;
    background: var(--back-text);
    opacity: 0.8;
  }
  .card-back .tagline {
    position: absolute;
    left: 110px;
    top: 216px;
    font-size: 16px;
    letter-spacing: 0.5px;
  }

  /* Front of card */
  .card-front {
    left: 110px;
    top: 520px;
    background: var(--paper);
    color: var(--ink);
  }
  .card-front .panel {
    position: absolute;
    inset: 0;
    width: 100%; height: 100%;
  }
  .card-front .brand {
    position: absolute;
    left: 300px;
    top: 34px;
    display: flex;
    align-items: center;
    gap: 10px;
  }
  .card-front .brand-dot {
    width: 22px; height: 22px;
    border-radius: 50%;
    background: var(--green);
  }
  .card-front .brand-name {
    font-weight: 700;
    font-size: 15px;
    color: var(--ink);
  }
  .card-front .name-banner {
    position: absolute;
    left: 200px;
    top: 96px;
    width: 200px;
    height: 36px;
    background: var(--green);
    clip-path: polygon(6% 0, 100% 0, 94% 100%, 0 100%);
    color: var(--white);
    font-size: 18px;
    letter-spacing: 0.4px;
    padding: 6px 0 0 24px;
  }
  .card-front .role {
    position: absolute;
    left: 218px; top: 138px;
    font-size: 13px;
  }
  .card-front .details {
    position: absolute;
    left: 210px; top: 170px;
    right: 24px;
    font-size: 11.5px;
    line-height: 1.5;
  }
  .card-front .address { margin-bottom: 4px; }
  .card-front .contact-grid {
    display: grid;
    grid-template-columns: 1fr 1fr;
    column-gap: 12px;
  }
  .card-front .contact { display: flex; align-items: center; gap: 6px; }
  .card-front .contact svg { width: 12px; height: 12px; flex: none; }
  .card-front .rule {
    position: absolute;
    left: 200px; top: 256px;
    width: 340px; height: 1.5px;
    background: var(--green-line);
  }
  .card-front .services {
    position: absolute;
    left: 206px; top: 264px;
    font-size: 13px;
    letter-spacing: 2.4px;
  }
  .card-front .services .sep { color: var(--green); }
</style>
</head>
<body>

<section class="card card-back" aria-label="Card back">
  <div class="brand">
    <span class="brand-dot"></span>
    <span class="brand-name">THE STONELYNK CO.</span>
  </div>
  <div class="rule-top"></div>
  <p class="website">www.stonelynk.ca</p>
  <p class="tagline">Crushing Solutions for your jobsite</p>
  <div class="rule-bottom"></div>
</section>

<section class="card card-front" aria-label="Card front">
  <svg class="panel" viewBox="0 0 560 320" preserveAspectRatio="none" aria-hidden="true">
    <polygon points="0,0 195,0 160,320 0,320" fill="var(--green)"/>
    <polygon points="150,0 195,0 160,320 150,320" fill="var(--green-light)"/>
  </svg>

  <div class="brand">
    <span class="brand-dot"></span>
    <span class="brand-name">THE STONELYNK CO.</span>
  </div>

  <div class="name-banner">DALE MORROW</div>
  <p class="role">Owner</p>

  <div class="details">
    <p class="address">2218 - 48B Avenue Nisku, Alberta T9E 1K2</p>
    <div class="contact-grid">
      <p class="contact">
        <svg viewBox="0 0 12 12"><path d="M2 1h2l1 3-1.5 1a7 7 0 0 0 3.5 3.5L8 7l3 1v2a1 1 0 0 1-1 1A9 9 0 0 1 1 2a1 1 0 0 1 1-1z" fill="var(--green)"/></svg>
        780 555 0142 (Direct)
      </p>
      <p class="contact">
        <svg viewBox="0 0 12 12"><rect x="1" y="4" width="10" height="6" fill="var(--green)"/><rect x="3" y="1" width="6" height="3" fill="var(--green)"/></svg>
        780 555 0196
      </p>
      <p class="contact">
        <svg viewBox="0 0 12 12"><path d="M2 1h2l1 3-1.5 1a7 7 0 0 0 3.5 3.5L8 7l3 1v2a1 1 0 0 1-1 1A9 9 0 0 1 1 2a1 1 0 0 1 1-1z" fill="var(--green)"/></svg>
        780 555 0178
      </p>
      <p class="contact">
        <svg viewBox="0 0 12 12"><rect x="1" y="2.5" width="10" height="7" fill="none" stroke="var(--green)" stroke-width="1.2"/><path d="M1 2.5l5 4 5-4" fill="none" stroke="var(--green)" stroke-width="1.2"/></svg>
        dale@stonelynk.com
      </p>
    </div>
  </div>

  <div class="rule"></div>
  <p class="services">Screeners <span class="sep">|</span> crushers <span class="sep">|</span> stackers</p>
</section>

</body>
</html>
```